IT Consulting company Needs a Logo Design and Business Cards

I need a New Logo and Business Cards for an established IT Managed Services Company that specializes in flat-rate managed IT services. We provide Design and Build, Help Desk, Onsite and Remote Support Services.

Target Market(s)

Corporate Clients

Industry/Entity Type

It Company

Logo Text

Halbrook Computer Group

Requirements
Nice to have
• Tag Line= Dependable IT, Done Right

```html
<!DOCTYPE html>
<html lang="en">
<head>
<meta charset="utf-8">
<title>Halbrook Computer Group – Business Cards</title>
<link href="https://fonts.googleapis.com/css2?family=Open+Sans:wght@400;600;700;800&display=swap" rel="stylesheet">
<style>
  :root{
    --page:#2b2b2d;
    --card-white:#ffffff;
    --card-black:#111112;
    --ink:#141414;
    --red:#d71f26;
    --orange:#f2a31b;
    --faint-light:#ececec;
    --faint-dark:#1b1b1d;
    --white:#ffffff;
  }
  *{box-sizing:border-box;margin:0;padding:0}
  html,body{width:1200px;height:900px;overflow:hidden}
  body{
    background:var(--page);
    font-family:"Open Sans",Arial,sans-serif;
    display:flex;flex-direction:column;align-items:center;justify-content:center;gap:40px;
  }
  .card{position:relative;width:700px;height:400px;overflow:hidden}

  /* Front */
  .card-front{background:var(--card-white);color:var(--ink)}
  .card-front .bottom-band{position:absolute;left:0;right:0;bottom:0;height:12px;background:var(--red)}
  .card-front .faint-circle{position:absolute;right:30px;top:-70px;width:250px;height:250px;border-radius:50%;border:34px solid var(--faint-light)}
  .brand{position:absolute;left:48px;top:58px;display:flex;align-items:center;gap:16px}
  .brand-dot{width:46px;height:46px;border-radius:50%;background:var(--red);flex:none}
  .brand-name{font-weight:800;font-size:27px;letter-spacing:1.5px;text-transform:uppercase;line-height:1.05;color:var(--ink)}
  .brand-tagline{font-weight:600;font-size:11px;letter-spacing:1.6px;text-transform:uppercase;color:var(--orange);margin-top:6px}
  .address{position:absolute;right:48px;top:205px;width:260px;text-align:right;font-size:13px;line-height:1.45;border-top:1px solid var(--orange);padding-top:10px}
  .divider{position:absolute;left:290px;top:205px;width:102px;height:1px;background:var(--ink)}
  .person{position:absolute;left:48px;top:186px}
  .person-name{font-weight:700;font-size:20px}
  .person-title{font-size:15px;color:var(--red);margin-top:2px}
  .contacts{position:absolute;left:48px;top:260px;list-style:none;font-size:14px}
  .contacts li{display:flex;align-items:center;gap:10px;height:24px}
  .icon{width:17px;height:17px;flex:none}

  /* Back */
  .card-back{background:var(--card-black);color:var(--white)}
  .card-back .faint-circle{position:absolute;right:-40px;top:-20px;width:360px;height:360px;border-radius:50%;border:46px solid var(--faint-dark)}
  .back-brand{position:absolute;left:150px;top:92px;display:flex;align-items:center;gap:20px}
  .back-brand .brand-dot{width:72px;height:72px}
  .back-brand .brand-name{font-size:36px;color:var(--white)}
  .back-brand .brand-tagline{font-size:14px}
  .services{position:absolute;left:0;right:0;bottom:64px;text-align:center;text-transform:uppercase}
  .services-lead{font-weight:700;font-size:19px;letter-spacing:.5px}
  .services-list{font-weight:700;font-size:19px;color:var(--red);margin-top:8px}
  .services-list .sep{color:var(--orange);margin:0 8px}
</style>
</head>
<body>

<section class="card card-front">
  <div class="faint-circle" aria-hidden="true"></div>
  <div class="brand">
    <div class="brand-dot" aria-hidden="true"></div>
    <div>
      <div class="brand-name">Halbrook<br>Computer Group</div>
      <div class="brand-tagline">Dependable IT, Done Right</div>
    </div>
  </div>
  <div class="divider" aria-hidden="true"></div>
  <p class="address">118 Larkin Street NE<br>Suite 210, Grand Rapids<br>MI 49505</p>
  <div class="person">
    <div class="person-name">Marcus Whitfield</div>
    <div class="person-title">CEO/Founder</div>
  </div>
  <ul class="contacts">
    <li>
      <svg class="icon" viewBox="0 0 17 17" aria-hidden="true"><rect width="17" height="17" rx="3" fill="#d71f26"/><path d="M5 4l2 .3.7 2.2-1.2.9a6 6 0 0 0 3 3l.9-1.2 2.2.7.3 2c-3.8.8-8.7-4.1-7.9-7.9z" fill="#fff"/></svg>
      214 555 0187
    </li>
    <li>
      <svg class="icon" viewBox="0 0 17 17" aria-hidden="true"><rect width="17" height="17" rx="3" fill="#d71f26"/><rect x="5" y="3.5" width="7" height="4" fill="#fff"/><rect x="3.5" y="7" width="10" height="5" rx="1" fill="#fff"/><rect x="5.5" y="10" width="6" height="3.5" fill="#fff" stroke="#d71f26" stroke-width=".8"/></svg>
      214 555 0187
    </li>
    <li>
      <svg class="icon" viewBox="0 0 17 17" aria-hidden="true"><rect width="17" height="17" rx="3" fill="#d71f26"/><rect x="3.5" y="5" width="10" height="7" fill="#fff"/><path d="M3.5 5l5 4 5-4" fill="none" stroke="#d71f26" stroke-width="1"/></svg>
      marcus@halbrookgroup.com
    </li>
    <li>
      <svg class="icon" viewBox="0 0 17 17" aria-hidden="true"><rect width="17" height="17" rx="3" fill="#d71f26"/><g fill="none" stroke="#fff" stroke-width="1"><circle cx="8.5" cy="8.5" r="5"/><ellipse cx="8.5" cy="8.5" rx="2.2" ry="5"/><path d="M3.5 8.5h10"/></g></svg>
      www.halbrookgroup.com
    </li>
  </ul>
  <div class="bottom-band" aria-hidden="true"></div>
</section>

<section class="card card-back">
  <div class="faint-circle" aria-hidden="true"></div>
  <div class="back-brand">
    <div class="brand-dot" aria-hidden="true"></div>
    <div>
      <div class="brand-name">Halbrook<br>Computer Group</div>
      <div class="brand-tagline">Dependable IT, Done Right</div>
    </div>
  </div>
  <div class="services">
    <p class="services-lead">Specializes in flat-rate managed IT services</p>
    <p class="services-list">Design and Build<span class="sep">•</span>Help Desk<span class="sep">•</span>Onsite and Remote Support</p>
  </div>
</section>

</body>
</html>
```